Etikettendesign für eine Grillsauce gesucht
Zielgruppe
Genuss aus dem Herzen der Schweiz
Kräuterbutter für Feinschmecker – dafür steht die Hubertsen’s Feinkost AG seit vielen Jahren. Mitten aus dem grünen Herzen der Schweiz verkündet die Hubertsen’s Feinkost AG ihre Genussbotschaft:
Der sorgsame Umgang mit den Rohstoffen der Natur ist die Grundlage für hochwertigen Genuss und vollmundigen Geschmack.
In jedem Produkt der Hubertsen’s Feinkost AG schmeckt man den Einklang mit der Natur: aromatisch, harmonisch, ausgewogen.
Aufgabenstellung
Eine neues Produkt soll entstehen.
- eine Grillsauce. Produktetikett für eine Flasche mit 500ml (welche noch nicht definiert ist) Es handelt sich hier um eine Lebensmitteletikette. Produktangaben wie Inhalte und Nährwerte werden auf dem Rücketikett stehen.
Wir brauchen das Designe für die Frontetikette.
Gestartet wird mit einer Sauce. Weitere Saucen sollen dann folgen.
- Lindo Sauce
- Chimichurri
- Café de Paris
- BBQ
Wir sind noch total in der Findung für ein neues Design. Was wir suchen ist ein Design welches sehr edel daher kommt und Lust auf mehr macht. Die Zielgruppe wird eher der Fleischkonsument und der Grillmeister sein.
Es darf im Vintage stil sein, soll aber elegant und edel wirken.
Es soll in Richtung Lifestyle Produkt gehen, welches der Metzger gerne in seinem Regal stehen hat oder das BBQ Restaurant auf den Tisch stellen will.
Eine Idee z.b. wäre, dass wir alle Saucen in die Roten Ketchup Quetflaschen abfüllen um ein alleinstellungsmerkmal zu haben.

```html
<!DOCTYPE html>
<html lang="de">
<head>
<meta charset="utf-8">
<title>Hubertsen’s Grillsauce – Frontetikette</title>
<link rel="stylesheet" href="https://fonts.googleapis.com/css2?family=Fira+Sans:wght@300;400;500;700&display=swap">
<style>
  :root {
    --page: #ffffff;
    --caramel: #b07a2a;
    --signal-red: #e30613;
    --outline-yellow: #f5e000;
    --cream: #f6ead6;
    --ink: #1e1e1e;
    --date-grey: #a8a8a8;
    --slate-dark: #3a3f47;
    --slate-mid: #5b606a;
    --sauce: #b8401c;
  }
  html, body {
    margin: 0;
    padding: 0;
    width: 1200px;
    height: 2400px;
    overflow: hidden;
    background: var(--page);
  }
  .label {
    position: absolute;
    left: 101px;
    top: 0;
    width: 2400px;
    height: 1017px;
    transform-origin: 0 0;
    transform: translate(1017px, 0) rotate(90deg);
    overflow: hidden;
    font-family: "Fira Sans", sans-serif;
    background: var(--caramel);
  }
  .label > * { position: absolute; margin: 0; }

  .product-photo {
    left: 1505px; top: 0; width: 895px; height: 1017px;
    background:
      radial-gradient(ellipse 360px 300px at 360px 300px, var(--sauce) 0%, #8a3a1c 55%, rgba(80,60,50,0) 75%),
      linear-gradient(135deg, var(--slate-mid) 0%, var(--slate-dark) 100%);
  }

  .brand-band {
    left: 122px; top: 97px; width: 1918px; height: 116px;
    background: var(--signal-red);
  }

  .reg-mark { left: 37px; top: 53px; width: 60px; height: 60px; }

  .brand-name {
    top: 97px;
    height: 116px;
    line-height: 116px;
    color: var(--page);
    font-size: 64px;
    font-weight: 500;
    letter-spacing: 1px;
    white-space: nowrap;
  }
  .brand-name--back { left: 470px; }
  .brand-name--front { left: 1560px; }

  .claim {
    left: 225px; top: 372px;
    font-size: 58px; font-weight: 700;
    color: var(--signal-red);
    -webkit-text-stroke: 1.5px #f3c98a;
    white-space: nowrap;
    letter-spacing: 0.5px;
  }

  .ingredients {
    top: 494px;
    color: var(--cream);
    font-size: 34px; font-weight: 300;
    line-height: 45px;
    white-space: nowrap;
  }
  .ingredients h3 { margin: 0; font-size: 34px; font-weight: 500; }
  .ingredients p { margin: 0; }
  .ingredients--de { left: 453px; }
  .ingredients--fr { left: 860px; }

  .address {
    left: 218px; top: 766px;
    color: var(--cream);
    font-size: 37px; font-weight: 400;
    white-space: nowrap;
  }

  .best-before {
    left: 330px; top: 858px; width: 428px;
    color: var(--cream);
    font-size: 33px; font-weight: 300;
    line-height: 42px;
    text-align: right;
  }
  .best-before p { margin: 0; }

  .date-field {
    left: 783px; top: 884px; width: 283px; height: 98px;
    background: var(--date-grey);
    border-radius: 18px;
  }

  .volume {
    color: var(--page);
    font-size: 82px; font-weight: 300;
    white-space: nowrap;
    line-height: 1;
  }
  .volume--back { left: 1103px; top: 906px; }
  .volume--front { left: 1757px; top: 906px; }

  .product-title {
    left: 1860px; top: 585px;
    font-size: 262px; font-weight: 700;
    color: var(--signal-red);
    -webkit-text-stroke: 5px var(--outline-yellow);
    letter-spacing: 10px;
    white-space: nowrap;
    line-height: 1;
  }
</style>
</head>
<body>
  <main class="label">
    <div class="product-photo" role="img" aria-label="Foto: Schale mit roter Grillsauce und Rosmarinzweig auf dunklem Schieferstein mit Salzkörnern"></div>

    <div class="brand-band"></div>

    <svg class="reg-mark" viewBox="0 0 60 60" aria-hidden="true">
      <circle cx="30" cy="30" r="26" fill="none" stroke="var(--ink)" stroke-width="4"/>
      <circle cx="30" cy="30" r="13" fill="none" stroke="var(--ink)" stroke-width="4"/>
    </svg>

    <div class="brand-name brand-name--back">Hubertsen’s Feinkost AG</div>

    <h2 class="claim">Genuss aus dem Herzen der Schweiz</h2>

    <section class="ingredients ingredients--de">
      <h3>Zutaten:</h3>
      <p>Tomaten, Essig,<br>Zucker, Zwiebeln,<br>Knoblauch, Salz,<br>Pfeffer.</p>
    </section>

    <section class="ingredients ingredients--fr">
      <h3>Ingrédients:</h3>
      <p>Tomates, vinaigre,<br>sucre, oignons,<br>ail, sel,<br>poivre.</p>
    </section>

    <div class="address">Hubertsen’s FEINKOST AG | Mühlegasse 9 | CH-6020 Emmenhof</div>

    <div class="best-before">
      <p>Mindestens Haltbar bis:</p>
      <p>À consommer de préférence</p>
      <p>avant:</p>
    </div>

    <div class="date-field"></div>

    <div class="volume volume--back">e 500 ml</div>

    <div class="brand-name brand-name--front">Hubertsen’s Feinkost AG</div>

    <h1 class="product-title">Grillsauce</h1>

    <div class="volume volume--front">500 ml</div>
  </main>
</body>
</html>
```